Electrical Contracting business website design

Website needed to help promote an online footprint focused on local customers in my area Gympie, QLD,Australia 4570

I am after a clear website (one where my customer does not get lost or frustrated)
most important is to engage customer to Call now or Request a quote with all the lead details.

Some bread and butter work for us is broken hot water units, electrical faults and renovators

We offer all sorts of services
- smoke alarms
- Test n Tag
- Lighting
- Fans
- A/C
- Design and planning
- safety switches
- underground Power
- Energy efficient solutions
- hot water repair
- Fault finding
- Control / Automation

Target Market(s)

Local Customers, Renovators, Builders, Commercial, Industrial, Domestic

Industry/Entity Type

Electrician

Coding

Coded - Design and coding required

Number of Pages Required

1 page

Colors
f78f20
000000
ec1f27
ffffff

Requirements
Must have
• Easy to use website with clear Contact Information (call now button)
• Ph: 0452916037 24/7
• Email Brightlinepower@mailnest.example
• , Quote request to receive leads and customer info

```html
<!DOCTYPE html>
<html lang="en">
<head>
<meta charset="utf-8">
<title>Brightline Power – Electrical Contracting</title>
<link rel="stylesheet" href="https://fonts.googleapis.com/css2?family=Fira+Sans:wght@400;500;600;700&family=Lato:wght@300;400;700&display=swap">
<style>
:root{
  --red:#ec1f27;
  --red-deep:#d3111a;
  --orange:#f78f20;
  --amber:#fdb913;
  --ink:#231f20;
  --dark:#231f20;
  --white:#ffffff;
  --grey:#555555;
  --head:"Fira Sans",sans-serif;
  --body:"Lato",sans-serif;
}
*{box-sizing:border-box;margin:0;padding:0}
html,body{width:1200px;height:3618px;overflow:hidden;background:var(--white)}
.page{position:relative;width:1200px;height:3618px;overflow:hidden;font-family:var(--body);color:var(--ink)}
.abs{position:absolute}

/* header */
.site-header{position:absolute;top:0;left:0;width:1200px;height:87px;background:var(--white);z-index:5}
.brand{position:absolute;left:94px;top:28px;display:flex;align-items:center;gap:8px;font-family:var(--head);font-weight:700;font-size:22px;color:var(--orange)}
.brand-dot{width:26px;height:26px;border-radius:50%;background:var(--red)}
.nav{position:absolute;left:517px;top:22px;display:flex;align-items:center;font-size:14px;font-family:var(--body)}
.nav a{text-decoration:none;color:var(--ink);padding:10px 22px}
.nav a.active{color:var(--orange);border:1.5px solid var(--orange);border-radius:22px;padding:10px 26px}
.btn{display:flex;align-items:center;justify-content:center;border-radius:24px;font-family:var(--head);font-weight:600;text-decoration:none}
.btn-call{position:absolute;left:988px;top:24px;width:118px;height:38px;color:var(--white);font-size:14px;background:linear-gradient(90deg,var(--amber),var(--orange) 45%,var(--red));box-shadow:0 3px 6px rgba(0,0,0,.2)}

/* hero */
.hero{position:absolute;top:87px;left:0;width:1200px;height:610px}
.hero-photo{position:absolute;left:590px;top:0;width:610px;height:489px;background:linear-gradient(135deg,#7a8b5a,#9aa6a0 45%,#4a5a7a)}
.hero-kicker{position:absolute;left:94px;top:184px;font-family:var(--head);font-weight:600;font-size:33px;color:var(--white)}
.hero-title{position:absolute;left:92px;top:210px;font-family:var(--head);font-weight:700;font-size:100px;color:var(--white);line-height:1.2}
.btn-quote{position:absolute;left:94px;top:343px;width:196px;height:48px;background:var(--white);color:var(--red);font-size:18px;box-shadow:0 4px 8px rgba(0,0,0,.25)}
.slider-arrow{position:absolute;top:445px;width:46px;height:46px;border-radius:50%;display:flex;align-items:center;justify-content:center}
.slider-prev{left:94px;border:2px solid var(--white)}
.slider-next{left:147px;background:var(--orange)}

/* help */
.help-photo{position:absolute;left:0;top:698px;width:640px;height:374px;border-radius:0 190px 190px 0 / 0 200px 200px 0;background:linear-gradient(160deg,#3d5a2e,#6f8a4a 45%,#22262a 70%,#8aa05a)}
.section-title{font-family:var(--head);font-weight:600;color:var(--ink);text-align:center}
.divider{display:flex;align-items:center;justify-content:center;gap:6px}
.divider i{display:block;width:30px;height:2px;background:var(--orange)}
.divider b{display:block;width:14px;height:14px;border-radius:50%;background:var(--red)}
.help-title{position:absolute;left:640px;top:744px;width:455px;font-size:47px}
.help-divider{position:absolute;left:640px;top:808px;width:455px}
.help-text{position:absolute;left:636px;top:848px;width:464px;text-align:center;font-weight:300;font-size:14px;line-height:21px;color:var(--grey)}
.btn-appt{position:absolute;left:700px;top:941px;width:203px;height:45px;color:var(--white);font-size:17px;background:linear-gradient(90deg,var(--amber),var(--orange) 40%,var(--red));box-shadow:0 3px 6px rgba(0,0,0,.2)}
.help-phone{position:absolute;left:922px;top:952px;font-family:var(--head);font-weight:500;font-size:18px;display:flex;align-items:center;gap:6px}

/* services */
.services{position:absolute;left:0;top:1060px;width:1200px;height:1200px}
.services-title{position:absolute;left:0;top:130px;width:1200px;font-size:47px;color:var(--white)}
.services-divider{position:absolute;left:0;top:196px;width:1200px}
.tile{position:absolute;width:194px;height:194px}
.tile-bg{position:absolute;left:28px;top:28px;width:138px;height:138px;transform:rotate(45deg);border-radius:8px}
.tile-body{position:absolute;inset:0;display:flex;flex-direction:column;align-items:center;justify-content:center;color:var(--white);font-family:var(--body);font-size:14px;text-align:center;line-height:17px;padding-top:4px}
.tile-icon{width:52px;height:52px;border-radius:50%;background:var(--white);margin-bottom:6px;display:flex;align-items:center;justify-content:center}
.hub{position:absolute;left:467px;top:542px;width:266px;height:266px;border-radius:50%;background:var(--white);display:flex;align-items:center;justify-content:center;font-family:var(--head);font-weight:700;font-size:24px;color:var(--red);text-align:center}

/* team */
.team-title{position:absolute;left:0;top:2276px;width:1200px;font-size:47px}
.team-divider{position:absolute;left:0;top:2335px;width:1200px}
.member{position:absolute;top:2412px;width:190px;text-align:center}
.member-photo{position:relative;margin:0 auto;width:173px;height:173px;background:linear-gradient(160deg,#c9ccd0,#7a8796 60%,#2e3a55);box-shadow:6px -6px 0 var(--orange)}
.member-name{margin-top:20px;font-family:var(--head);font-weight:500;font-size:18px;color:var(--ink)}
.member-role{font-size:13px;color:var(--grey);font-weight:300}
.member-bio{margin-top:6px;font-size:12.5px;line-height:19px;color:var(--grey);font-weight:300}
.socials{display:flex;gap:6px;justify-content:center;margin-top:14px}
.socials span{width:27px;height:27px;border-radius:50%;background:linear-gradient(180deg,var(--amber),var(--orange));box-shadow:0 1px 3px rgba(0,0,0,.3)}

/* quote */
.quote-title{position:absolute;left:92px;top:2990px;font-family:var(--head);font-weight:600;font-size:45px;color:var(--white)}
.quote-divider{position:absolute;left:92px;top:3052px;width:348px}
.field{position:absolute;top:2994px;width:320px;height:49px;border-radius:25px;background:var(--white);display:flex;align-items:center;padding-left:14px;gap:6px;font-size:12px;color:#666}
.btn-submit{position:absolute;left:989px;top:3053px;width:119px;height:42px;color:var(--white);font-size:18px;background:linear-gradient(90deg,var(--amber),var(--orange));box-shadow:0 3px 6px rgba(0,0,0,.25)}

/* footer */
.foot-brand{position:absolute;left:94px;top:3376px;display:flex;align-items:center;gap:12px;font-family:var(--head);font-weight:700;font-size:30px;color:var(--orange)}
.foot-brand .brand-dot{width:40px;height:40px}
.foot-h{position:absolute;font-family:var(--head);font-weight:500;font-size:19px;color:var(--white)}
.foot-list{position:absolute;top:3366px;list-style:none;font-size:12.5px;color:#b9b9b9;line-height:30.2px}
.foot-phone{position:absolute;left:853px;top:3350px;font-family:var(--head);font-weight:600;font-size:31px;color:var(--red)}
.foot-email{position:absolute;left:853px;top:3410px;font-family:var(--head);font-size:16px;color:var(--white);display:flex;align-items:center;gap:6px}
.foot-addr{position:absolute;left:875px;top:3432px;font-size:13px;color:#b9b9b9}
.follow{position:absolute;left:93px;top:3512px;display:flex;align-items:center;gap:8px;font-family:var(--head);font-size:19px;color:var(--white)}
.follow .socials{margin:0 0 0 14px;gap:8px}
.follow .socials span{width:37px;height:37px}
.copy{position:absolute;left:839px;top:3520px;font-size:12px;color:#b9b9b9}
.copy em{font-style:normal;color:var(--orange)}
</style>
</head>
<body>
<div class="page">

<header class="site-header">
  <div class="brand"><span class="brand-dot"></span>Brightline Power</div>
  <nav class="nav">
    <a class="active" href="#">Home</a><a href="#">About</a><a href="#">Services</a><a href="#">Our Team</a><a href="#">Contact</a>
  </nav>
  <a class="btn btn-call" href="#">Call Now</a>
</header>

<section class="hero">
  <svg class="abs" style="left:0;top:0" width="1200" height="610" viewBox="0 0 1200 610">
    <rect width="1200" height="610" fill="var(--red)"/>
    <path d="M0,590 C300,510 700,490 900,500 C1030,505 1130,540 1200,600 L1200,610 L0,610 Z" fill="var(--white)"/>
    <path d="M0,590 C300,510 700,492 900,490 C1030,490 1130,520 1200,600" fill="none" stroke="var(--orange)" stroke-width="6"/>
    <path d="M0,600 C300,525 700,505 900,505" fill="none" stroke="#b5121a" stroke-width="3"/>
  </svg>
  <div class="hero-photo" role="img" aria-label="Photo of two electricians standing together outdoors at a work site"></div>
  <div class="hero-kicker">Electrical Contracting</div>
  <h1 class="hero-title">Business</h1>
  <a class="btn btn-quote" href="#">Request a Quote</a>
  <span class="slider-arrow slider-prev"><svg width="14" height="14" viewBox="0 0 14 14"><path d="M9 2 L4 7 L9 12" stroke="#fff" stroke-width="2.5" fill="none"/></svg></span>
  <span class="slider-arrow slider-next"><svg width="14" height="14" viewBox="0 0 14 14"><path d="M5 2 L10 7 L5 12" stroke="var(--red)" stroke-width="2.5" fill="none"/></svg></span>
</section>

<section>
  <div class="help-photo" role="img" aria-label="Photo of the company work truck with ladder rack and a trailer parked on grass"></div>
  <h2 class="section-title help-title">How We Can Help</h2>
  <div class="divider help-divider"><i></i><b></b><i></i></div>
  <p class="help-text">Aliquam egestas tortor et est dapibus, id interdum nisi pulvinar. Morbi ultricies quam quis mattis sagittis. Nulla rutrum arcu in leo fermentum, quis fringilla urna tristique. Fusce scelerisque, libero eu faucibus fringilla</p>
  <a class="btn btn-appt" href="#">Make an Appoinment</a>
  <div class="help-phone"><svg width="14" height="16" viewBox="0 0 14 16"><path d="M3 1 L6 4 L4.5 6 C5.5 8.5 7 10 9 11 L11 9.5 L13.5 12.5 L11.5 15 C6 14 1.5 9 1 3 Z" fill="var(--orange)"/></svg>0452916037</div>
</section>

<section class="services">
  <svg class="abs" style="left:0;top:0" width="1200" height="1200" viewBox="0 0 1200 1200">
    <path d="M0,250 C40,150 120,90 240,72 L1200,72 L1200,140 Z" fill="var(--orange)"/>
    <path d="M0,300 C40,170 130,72 280,72 L1200,72 L1200,1000 C1100,1080 950,1139 760,1139 L0,1139 Z" fill="var(--red-deep)"/>
  </svg>

  <h2 class="section-title services-title">Repairs &amp; Services</h2>
  <div class="divider services-divider"><i></i><b style="background:var(--amber)"></b><i></i></div>

  <div class="tile" style="left:504px;top:252px"><div class="tile-bg" style="background:linear-gradient(135deg,#f35c1f,#f78f20)"></div><div class="tile-body"><span class="tile-icon"><svg width="30" height="30"><circle cx="15" cy="15" r="12" fill="none" stroke="#888" stroke-width="2"/><circle cx="15" cy="15" r="6" fill="none" stroke="#888" stroke-width="2"/></svg></span>Smoke Alarms</div></div>
  <div class="tile" style="left:613px;top:360px"><div class="tile-bg" style="background:linear-gradient(135deg,#b0203a,#f78f20)"></div><div class="tile-body"><span class="tile-icon"><svg width="30" height="30"><rect x="8" y="8" width="14" height="14" transform="rotate(45 15 15)" fill="none" stroke="#888" stroke-width="2"/></svg></span>Test n Tag</div></div>
  <div class="tile" style="left:395px;top:360px"><div class="tile-bg" style="background:linear-gradient(135deg,#2bd46a,#1ec6e6)"></div><div class="tile-body"><span class="tile-icon"><svg width="30" height="30"><circle cx="15" cy="15" r="8" fill="none" stroke="#888" stroke-width="2"/><circle cx="15" cy="15" r="3" fill="#888"/></svg></span>Control /<br>Automation</div></div>
  <div class="tile" style="left:284px;top:470px"><div class="tile-bg" style="background:linear-gradient(135deg,#2e9e3a,#7ed957)"></div><div class="tile-body"><span class="tile-icon"><svg width="30" height="30"><circle cx="10" cy="17" r="5" fill="none" stroke="#888" stroke-width="2"/><circle cx="20" cy="17" r="5" fill="none" stroke="#888" stroke-width="2"/></svg></span>Fault Finding</div></div>
  <div class="tile" style="left:725px;top:470px"><div class="tile-bg" style="background:linear-gradient(135deg,#9b2a7a,#e0307a)"></div><div class="tile-body"><span class="tile-icon"><svg width="30" height="30"><path d="M15 4 a8 8 0 0 1 5 14 v4 h-10 v-4 a8 8 0 0 1 5 -14z M11 25 h8" fill="none" stroke="#888" stroke-width="2"/></svg></span>Lighting</div></div>
  <div class="tile" style="left:174px;top:581px"><div class="tile-bg" style="background:linear-gradient(135deg,#f4a11a,#fdd33a)"></div><div class="tile-body"><span class="tile-icon"><svg width="30" height="30"><rect x="9" y="4" width="12" height="22" rx="3" fill="none" stroke="#888" stroke-width="2"/></svg></span>Hot Water<br>Repair</div></div>
  <div class="tile" style="left:833px;top:581px"><div class="tile-bg" style="background:linear-gradient(135deg,#f2385a,#f78f20)"></div><div class="tile-body"><span class="tile-icon"><svg width="30" height="30"><circle cx="15" cy="15" r="11" fill="none" stroke="#888" stroke-width="2"/><path d="M15 15 L15 6 M15 15 L23 19 M15 15 L7 19" stroke="#888" stroke-width="2"/></svg></span>Fans</div></div>
  <div class="tile" style="left:285px;top:692px"><div class="tile-bg" style="background:linear-gradient(135deg,#0fa38a,#8ad44a)"></div><div class="tile-body"><span class="tile-icon"><svg width="30" height="30"><path d="M16 4 L10 15 H15 L13 25 L21 12 H16 Z" fill="#888"/></svg></span>Energy Efficient<br>Solutions</div></div>
  <div class="tile" style="left:725px;top:692px"><div class="tile-bg" style="background:linear-gradient(135deg,#1fa85a,#a6d94a)"></div><div class="tile-body"><span class="tile-icon"><svg width="30" height="30"><rect x="4" y="9" width="22" height="9" rx="2" fill="none" stroke="#888" stroke-width="2"/></svg></span>A/C</div></div>
  <div class="tile" style="left:395px;top:802px"><div class="tile-bg" style="background:linear-gradient(135deg,#1a4fa8,#19a3d8)"></div><div class="tile-body"><span class="tile-icon"><svg width="30" height="30"><path d="M15 5 L26 24 H4 Z" fill="none" stroke="#888" stroke-width="2"/></svg></span>Underground<br>Power</div></div>
  <div class="tile" style="left:613px;top:802px"><div class="tile-bg" style="background:linear-gradient(135deg,#7a4ee0,#3aa0e8)"></div><div class="tile-body"><span class="tile-icon"><svg width="30" height="30"><rect x="8" y="4" width="14" height="22" fill="none" stroke="#888" stroke-width="2"/><path d="M11 10h8M11 15h8M11 20h5" stroke="#888" stroke-width="2"/></svg></span>Design and<br>planning</div></div>
  <div class="tile" style="left:504px;top:910px"><div class="tile-bg" style="background:linear-gradient(135deg,#5a3fb0,#19b0d8)"></div><div class="tile-body"><span class="tile-icon"><svg width="30" height="30"><rect x="9" y="4" width="12" height="22" rx="2" fill="none" stroke="#888" stroke-width="2"/></svg></span>Safety<br>Switches</div></div>

  <div class="hub">Brightline<br>Power</div>
</section>

<section>
  <h2 class="section-title team-title">Meet Our Team</h2>
  <div class="divider team-divider"><i></i><b></b><i></i></div>

  <article class="member" style="left:88px"><div class="member-photo" role="img" aria-label="Photo of an electrician working at a switchboard"></div><h3 class="member-name">Vestibulum vel</h3><p class="member-role">Lorem ipsum</p><p class="member-bio">Lorem ipsum dolor sit amet, consectetur adipiscing elit. Pellentesque pharetra blandit sollicitudin. Phasellus ultricies ex ut semper blandit.</p><div class="socials"><span></span><span></span><span></span></div></article>
  <article class="member" style="left:297px"><div class="member-photo" role="img" aria-label="Photo of an electrician in a hard hat holding a meter"></div><h3 class="member-name">Vestibulum vel</h3><p class="member-role">Lorem ipsum</p><p class="member-bio">Lorem ipsum dolor sit amet, consectetur adipiscing elit. Pellentesque pharetra blandit sollicitudin. Phasellus ultricies ex ut semper blandit.</p><div class="socials"><span></span><span></span><span></span></div></article>
  <article class="member" style="left:505px"><div class="member-photo" role="img" aria-label="Photo of an electrician in a hard hat reading plans"></div><h3 class="member-name">Vestibulum vel</h3><p class="member-role">Lorem ipsum</p><p class="member-bio">Lorem ipsum dolor sit amet, consectetur adipiscing elit. Pellentesque pharetra blandit sollicitudin. Phasellus ultricies ex ut semper blandit.</p><div class="socials"><span></span><span></span><span></span></div></article>
  <article class="member" style="left:713px"><div class="member-photo" role="img" aria-label="Photo of an electrician in a hard hat holding a drill"></div><h3 class="member-name">Vestibulum vel</h3><p class="member-role">Lorem ipsum</p><p class="member-bio">Lorem ipsum dolor sit amet, consectetur adipiscing elit. Pellentesque pharetra blandit sollicitudin. Phasellus ultricies ex ut semper blandit.</p><div class="socials"><span></span><span></span><span></span></div></article>
  <article class="member" style="left:922px"><div class="member-photo" role="img" aria-label="Photo of an electrician standing with arms crossed"></div><h3 class="member-name">Vestibulum vel</h3><p class="member-role">Lorem ipsum</p><p class="member-bio">Lorem ipsum dolor sit amet, consectetur adipiscing elit. Pellentesque pharetra blandit sollicitudin. Phasellus ultricies ex ut semper blandit.</p><div class="socials"><span></span><span></span><span></span></div></article>
</section>

<section>
  <svg class="abs" style="left:0;top:2860px" width="1200" height="758" viewBox="0 0 1200 758">
    <path d="M0,120 C60,40 140,17 260,17 L1200,17 L1200,758 L0,758 Z" fill="var(--orange)"/>
    <path d="M0,140 C60,50 160,17 300,17 L1200,17 L1200,758 L0,758 Z" fill="var(--red)"/>
    <path d="M0,310 C300,370 700,360 1200,300 L1200,758 L0,758 Z" fill="var(--orange)" opacity=".8"/>
    <path d="M0,330 C300,390 700,385 1200,320 L1200,758 L0,758 Z" fill="var(--white)"/>
    <path d="M0,345 C300,405 700,400 1200,335 L1200,758 L0,758 Z" fill="var(--dark)"/>
  </svg>
  <h2 class="quote-title">Get A Fee Quote</h2>
  <div class="divider quote-divider"><i style="background:var(--amber)"></i><b style="background:var(--amber)"></b><i style="background:var(--amber)"></i></div>
  <label class="field" style="left:457px"><svg width="14" height="14"><circle cx="7" cy="4.5" r="3.3" fill="none" stroke="#777"/><path d="M1 13 C2 8 12 8 13 13" fill="none" stroke="#777"/></svg>Name</label>
  <label class="field" style="left:788px"><svg width="16" height="12"><rect x=".5" y=".5" width="15" height="11" fill="none" stroke="#777"/><path d="M1 1 L8 7 L15 1" fill="none" stroke="#777"/></svg>Email address</label>
  <a class="btn btn-submit" href="#">Submit</a>
</section>

<footer>
  <div class="foot-brand"><span class="brand-dot"></span>Brightline Power</div>
  <h4 class="foot-h" style="left:479px;top:3322px">Services</h4>
  <ul class="foot-list" style="left:480px"><li>Smoke Alarms</li><li>Test n Tag</li><li>Lighting</li><li>Fans</li><li>A/C</li><li>Design and planning</li></ul>
  <ul class="foot-list" style="left:638px"><li>Safety Switches</li><li>Underground Power</li><li>Energy Efficient Solutions</li><li>Hot Water Repair</li><li>Fault finding</li><li>Control / Automation</li></ul>
  <h4 class="foot-h" style="left:853px;top:3320px">Call Now for Services! (24x7)</h4>
  <div class="foot-phone">0452916037</div>
  <div class="foot-email"><svg width="18" height="13"><rect width="18" height="13" fill="var(--orange)"/><path d="M0 0 L9 7 L18 0" fill="none" stroke="#fff"/></svg>Email Us</div>
  <div class="foot-addr">Brightlinepower@mailnest.example</div>
  <div class="follow">Follow Us<div class="socials"><span></span><span></span><span></span></div></div>
  <p class="copy">© 2019 <em>Brightline Power</em>. All Right Reserved.</p>
</footer>

</div>
</body>
</html>
```